Executive Taxi firm with Chauffeur service Website

I have my domain name registered and I have started to work on my site but I am struggling. I am just about to get a logo for the company and need a web site that clearly represents the fact we are an executive/luxury brand in private hire vehicles. We offer airport transfers, train station transfers, seaport transfers, holiday transfers and business to business pick up and drop off.

Target Market(s)

Corporate people, holidaymakers looking for a luxury start their holiday. VIPs' and celebrities.

Number of Pages Required

5+ page

Font styles to use
Serif
Sans Serif
Decorative
Script

Colors

Designer to choose colors to be used in the design.

Requirements
Must have
• Home Page, Services, About Us, VIP and Contact us
• Please see www.brookvane.co.uk I have started it but not happy with it at all.
Nice to have
• Booking form or enquiry form.

```html
<!DOCTYPE html>
<html lang="en">
<head>
<meta charset="utf-8">
<title>Brookvane — Private Hire, Chauffeur and Taxi Service</title>
<link href="https://fonts.googleapis.com/css2?family=Roboto:wght@300;400;500;700&display=swap" rel="stylesheet">
<style>
:root{
  --red:#c8102e;
  --dark:#1c1c1c;
  --ink:#222;
  --text:#444;
  --muted:#777;
  --line:#dcdcdc;
  --soft:#f2f2f2;
  --white:#fff;
}
*{box-sizing:border-box;margin:0;padding:0}
html,body{width:1200px;height:3879px;overflow:hidden}
body{font-family:"Roboto",Arial,sans-serif;color:var(--ink);background:var(--white);position:relative}
.abs{position:absolute}
.btn-outline{position:absolute;border:2px solid var(--red);color:var(--ink);font-size:11px;font-weight:700;letter-spacing:.5px;display:flex;align-items:center;justify-content:center;background:var(--white)}
.btn-red{position:absolute;background:var(--red);color:var(--white);font-weight:700;display:flex;align-items:center;justify-content:center}
.section-title{position:absolute;left:0;width:1200px;text-align:center;font-size:28px;font-weight:300;color:var(--ink)}

/* hero */
.hero{position:absolute;left:0;top:0;width:1200px;height:559px;background:linear-gradient(100deg,#2a2726 0%,#4a423d 40%,#3a3634 65%,#191919 100%)}
.hero-shade{position:absolute;inset:0;background:rgba(0,0,0,.28)}
.brand{position:absolute;left:111px;top:40px;display:flex;align-items:center;gap:10px;color:var(--white);font-size:26px;font-weight:400}
.brand-dot{width:30px;height:30px;border-radius:50%;border:3px solid var(--white)}
.nav{position:absolute;top:48px;left:708px;display:flex;gap:34px;font-size:15px;color:var(--white)}
.hero-title{position:absolute;top:248px;width:1200px;text-align:center;color:var(--white);font-size:33px;font-weight:300;line-height:40px;letter-spacing:.5px}
.hero-sub{position:absolute;top:342px;width:1200px;text-align:center;color:var(--white);font-size:15px;letter-spacing:.5px}
.hero-btn{position:absolute;left:515px;top:397px;width:127px;height:32px;border:2px solid var(--white);background:#111;color:var(--white);font-size:12px;font-weight:700;display:flex;align-items:center;justify-content:center}
.arrow{position:absolute;top:303px;width:36px;height:36px;border-radius:50%;background:#d9d9d9;display:flex;align-items:center;justify-content:center}

/* booking */
.booking{position:absolute;left:752px;top:502px;width:334px;height:378px;background:var(--white);box-shadow:0 2px 10px rgba(0,0,0,.18)}
.tabs{display:flex;height:57px}
.tab{flex:1;display:flex;align-items:center;justify-content:center;font-size:15px;color:var(--white);background:#3a3a3a}
.tab.active{background:var(--red)}
.field{position:absolute;left:17px;width:300px;height:38px;border:1px solid var(--line);font-size:12px;color:#999;padding:0 10px;display:flex;align-items:center}
.time-label{position:absolute;left:17px;top:255px;font-size:13px;color:var(--ink)}
.select{position:absolute;top:241px;width:108px;height:36px;border:1px solid var(--line);font-size:11px;color:#999;display:flex;align-items:center;justify-content:space-between;padding:0 10px}

/* welcome */
.welcome h1{position:absolute;left:111px;top:590px;font-size:29px;font-weight:300}
.welcome h1 span{color:var(--red)}
.welcome p{position:absolute;left:111px;width:570px;font-size:12.5px;line-height:25px;color:var(--text)}

/* services */
.card-photo{position:absolute;width:225px;height:163px}
.card-title{position:absolute;font-size:15px;font-weight:700;color:var(--ink)}
.card-text{position:absolute;width:215px;font-size:11.5px;line-height:19px;color:var(--text)}

/* b2b */
.feature-panel{position:absolute;left:111px;top:1484px;width:290px;height:445px;background:linear-gradient(160deg,#f5f5f5,#e9dede 60%,#d9a7a7);box-shadow:0 2px 8px rgba(0,0,0,.15)}
.feature{position:absolute;left:0;width:290px;text-align:center;font-size:17px;color:var(--ink)}
.b2b-photo{position:absolute;left:421px;top:1484px;width:668px;height:347px;background:linear-gradient(120deg,#1d1d1f,#4a4a4e 45%,#2b2b2e 70%,#8a8a8a)}
.b2b-title{position:absolute;left:421px;top:1846px;font-size:21px;font-weight:300;letter-spacing:.3px}
.b2b-text{position:absolute;left:421px;top:1878px;width:640px;font-size:12px;line-height:26px;color:var(--text)}

/* why */
.why{position:absolute;width:230px;text-align:center}
.why h3{font-size:19px;font-weight:500;margin-top:14px}
.why p{font-size:12px;line-height:20px;color:var(--text);margin-top:6px;padding:0 28px}
.why-box{position:absolute;left:358px;top:2165px;width:229px;height:162px;border:1px solid #e0b0b0;box-shadow:0 2px 8px rgba(0,0,0,.12)}

/* fleet */
.fleet-bg{position:absolute;left:0;top:2405px;width:1200px;height:572px;background:var(--soft)}
.fleet-photo{position:absolute;top:2563px;width:225px;height:157px;background:var(--white);display:flex;align-items:center;justify-content:center}
.car-shape{width:160px;height:60px;border-radius:40px 50px 14px 14px}
.price{position:absolute;top:2729px;height:24px;padding:0 10px;background:var(--red);color:var(--white);font-size:11px;font-weight:700;display:flex;align-items:center}
.car-name{position:absolute;top:2763px;font-size:14px;font-weight:700}
.car-spec{position:absolute;font-size:11px;color:var(--text);display:flex;align-items:center;gap:10px}
.car-spec i{width:8px;height:8px;border-radius:50%;background:var(--ink);display:block}

/* cta */
.cta{position:absolute;left:0;top:2977px;width:1200px;height:230px;background:linear-gradient(90deg,#2b2b2b,#4c4c4c 50%,#2a2a2a)}
.cta h2{position:absolute;top:73px;width:1200px;text-align:center;color:var(--white);font-size:23px;font-weight:400;letter-spacing:.4px}

/* contact */
.info{position:absolute;left:126px;width:400px;text-align:center}
.info h4{font-size:15px;font-weight:700;letter-spacing:.5px}
.info p{font-size:12.5px;line-height:29px;color:var(--ink);margin-top:6px}
.social{position:absolute;top:3619px;width:34px;height:34px;border:1px solid var(--red);display:flex;align-items:center;justify-content:center}
.social i{display:block;width:10px;height:10px;background:var(--ink)}
.contact-title{position:absolute;left:613px;top:3304px;font-size:15px;font-weight:700}
.input{position:absolute;left:613px;width:476px;border:1px solid var(--line);font-size:11px;color:#999;padding:0 10px;display:flex;align-items:center}

/* footer */
.footer{position:absolute;left:0;top:3716px;width:1200px;height:163px;background:var(--dark)}
.footer .brand{top:52px}
.footer .nav{top:63px;font-size:14px}
.copy{position:absolute;left:111px;top:103px;font-size:11px;color:#bbb}
</style>
</head>
<body>

<header class="hero">
  <div class="abs" role="img" aria-label="Chauffeur opening a luxury car door for a smiling passenger" style="inset:0"></div>
  <div class="hero-shade"></div>
  <div class="brand"><span class="brand-dot"></span>Brookvane</div>
  <nav class="nav"><span>Home</span><span>Services</span><span>About Us</span><span>VIP</span><span>Contact us</span></nav>
  <div class="hero-title">PRIVATE HIRE, CHAUFFEUR AND TAXI SERVICE<br>EXECUTIVE BROOKVANE TRAVEL</div>
  <div class="hero-sub">WE PICK UP &amp; DROP YOU ON TIME BY BEST TARIFF</div>
  <div class="hero-btn">BOOK NOW</div>
  <div class="arrow" style="left:96px"><svg width="12" height="12" viewBox="0 0 12 12"><path d="M8 1 3 6l5 5" fill="none" stroke="#333" stroke-width="2.4"/></svg></div>
  <div class="arrow" style="left:1066px"><svg width="12" height="12" viewBox="0 0 12 12"><path d="M4 1l5 5-5 5" fill="none" stroke="#333" stroke-width="2.4"/></svg></div>
</header>

<section class="booking">
  <div class="tabs"><div class="tab active">One way Transfer</div><div class="tab">Hourly Service</div></div>
  <div class="field" style="top:77px">Pick Up address</div>
  <div class="field" style="top:128px">Drop Off address</div>
  <div class="field" style="top:180px">31/10/2018</div>
  <div class="time-label">Pick up Time</div>
  <div class="select" style="left:127px">12am <span>▾</span></div>
  <div class="select" style="left:209px">00 <span>▾</span></div>
  <div class="btn-red" style="left:17px;top:300px;width:300px;height:38px;font-size:15px;font-weight:500">Reserve Now</div>
</section>

<section class="welcome">
  <h1>Welcome To <span>Brookvane</span></h1>
  <p style="top:640px">We provide airport transfers to and from all major UK airports, seaports, train station transfers and an executive business to business transfer service. Whether you have an individual or group transfer request, our company-owned fleet offers a choice of options to suit your needs, from luxury saloons and SUV's to 9-seat luxury transporters.</p>
  <p style="top:741px">We provide a door-to-door convenience from your home, office or hotel straight to any destination of your choice. Pre-booked or last minute we aim to cover any transport requirement. Allports and train station service; All pickups from arrivals will of been briefed as to your exact pickup point,</p>
  <div class="btn-outline" style="left:111px;top:836px;width:124px;height:31px">READ MORE</div>
</section>

<section class="services">
  <h2 class="section-title" style="top:942px">Our Services</h2>
  <div class="card-photo" role="img" aria-label="Chauffeur greeting a traveller at the airport" style="left:111px;top:1014px;background:linear-gradient(135deg,#cfcfcf,#6f7780)"></div>
  <div class="card-photo" role="img" aria-label="Train station platform with a train" style="left:362px;top:1014px;background:linear-gradient(135deg,#8a9096,#3c434a)"></div>
  <div class="card-photo" role="img" aria-label="Classic red car by a sunny seaport" style="left:610px;top:1014px;background:linear-gradient(135deg,#5fb3d9,#b84a3c 70%,#d9c49a)"></div>
  <div class="card-photo" role="img" aria-label="Open road at sunset for a holiday drive" style="left:861px;top:1014px;background:linear-gradient(135deg,#f0b35a,#a0552a 60%,#3a2418)"></div>

  <div class="card-title" style="left:119px;top:1190px">Airport transfers</div>
  <div class="card-title" style="left:370px;top:1190px">Train station transfers</div>
  <div class="card-title" style="left:618px;top:1190px">Seaport transfers</div>
  <div class="card-title" style="left:869px;top:1190px">Holiday transfers</div>

  <div class="card-text" style="left:119px;top:1222px">Excepteur sint occaecat cupidatat non proident, sunt in culpa qui officia deserunt mollit anim ...</div>
  <div class="card-text" style="left:370px;top:1222px">Excepteur sint occaecat cupidatat non proident, sunt in culpa qui officia deserunt mollit anim ...</div>
  <div class="card-text" style="left:618px;top:1222px">Excepteur sint occaecat cupidatat non proident, sunt in culpa qui officia deserunt mollit anim ...</div>
  <div class="card-text" style="left:869px;top:1222px">Excepteur sint occaecat cupidatat non proident, sunt in culpa qui officia deserunt mollit anim ...</div>

  <div class="btn-outline" style="left:119px;top:1302px;width:106px;height:29px">READ MORE</div>
  <div class="btn-outline" style="left:370px;top:1302px;width:106px;height:29px">READ MORE</div>
  <div class="btn-outline" style="left:618px;top:1302px;width:106px;height:29px">READ MORE</div>
  <div class="btn-outline" style="left:869px;top:1302px;width:106px;height:29px">READ MORE</div>
</section>

<section class="b2b">
  <h2 class="section-title" style="top:1415px">Business to Business Pick Up and Drop Off</h2>
  <div class="feature-panel">
    <svg class="abs" style="left:112px;top:42px" width="66" height="32" viewBox="0 0 66 32"><path d="M4 22v-6l8-2 8-9h24l10 9 8 2v6z" fill="none" stroke="#222" stroke-width="2.5"/><circle cx="17" cy="24" r="5" fill="#fff" stroke="#222" stroke-width="2.5"/><circle cx="49" cy="24" r="5" fill="#fff" stroke="#222" stroke-width="2.5"/></svg>
    <div class="feature" style="top:102px">Luxury Car</div>
    <svg class="abs" style="left:108px;top:172px" width="72" height="34" viewBox="0 0 72 34"><path d="M2 10h16M6 16h12M2 22h14" stroke="#222" stroke-width="2.5"/><path d="M20 24v-6l8-2 7-8h20l8 8 7 2v6z" fill="none" stroke="#222" stroke-width="2.5"/><circle cx="32" cy="26" r="4.5" fill="#fff" stroke="#222" stroke-width="2.5"/><circle cx="58" cy="26" r="4.5" fill="#fff" stroke="#222" stroke-width="2.5"/></svg>
    <div class="feature" style="top:232px">Fast &amp; Safe</div>
    <svg class="abs" style="left:125px;top:295px" width="44" height="50" viewBox="0 0 44 50"><rect x="3" y="3" width="38" height="44" fill="none" stroke="#222" stroke-width="2.5"/><path d="M10 14h6M10 25h6M10 36h6M21 14h13M21 25h13M21 36h13" stroke="#222" stroke-width="2.5"/></svg>
    <div class="feature" style="top:362px">Best Tariff</div>
  </div>
  <div class="b2b-photo" role="img" aria-label="Businessman in a suit stepping out of an executive car"></div>
  <div class="b2b-title">ON TIME PICK-UP &amp; DROP BY EXPERIENCED CAB DRIVERS</div>
  <div class="b2b-text">Donec varius sodales orci. Class aptent taciti sociosqu ad litora torquent per conubia nostra, per inceptos himenaeos. Aenean a arcu ullamcorper eros viverra suscipit. Donec varius</div>
</section>

<section class="why-us">
  <div class="abs" style="left:0;top:1986px;width:1200px;height:419px;background:#fafafa"></div>
  <h2 class="section-title" style="top:2033px">Why Choose Us</h2>
  <div class="why-box"></div>
  <svg class="abs" style="left:428px;top:2118px" width="90" height="48" viewBox="0 0 90 48"><path d="M4 48A41 41 0 0 1 86 48" fill="none" stroke="#c8102e" stroke-width="8"/></svg>

  <div class="why" style="left:107px;top:2140px">
    <svg width="44" height="44" viewBox="0 0 44 44"><rect x="8" y="4" width="24" height="32" fill="none" stroke="#222" stroke-width="2.5"/><path d="M13 12h14M13 19h14M13 26h8" stroke="#222" stroke-width="2.5"/><circle cx="32" cy="32" r="8" fill="#fff" stroke="#222" stroke-width="2.5"/><path d="M28 32l3 3 5-5" fill="none" stroke="#222" stroke-width="2.5"/></svg>
    <h3>FAST BOOKING</h3>
    <p>Donec varius sodales orci. Class aptent taciti sociosqu ad litora torquent per conubia</p>
  </div>
  <div class="why" style="left:358px;top:2140px">
    <svg width="44" height="44" viewBox="0 0 44 44"><path d="M22 40S10 26 10 17a12 12 0 0 1 24 0c0 9-12 23-12 23z" fill="none" stroke="#222" stroke-width="2.5"/><circle cx="22" cy="17" r="4" fill="none" stroke="#222" stroke-width="2.5"/></svg>
    <h3>TRACKING DEVICES</h3>
    <p>Donec varius sodales orci. Class aptent taciti sociosqu ad litora torquent per conubia</p>
  </div>
  <div class="why" style="left:609px;top:2140px">
    <svg width="44" height="44" viewBox="0 0 44 44"><circle cx="22" cy="24" r="15" fill="none" stroke="#222" stroke-width="2.5"/><path d="M22 15v10l6 4M6 10l6-5M38 10l-6-5" fill="none" stroke="#222" stroke-width="2.5"/></svg>
    <h3>ON TIME ARRIVAL</h3>
    <p>Donec varius sodales orci. Class aptent taciti sociosqu ad litora torquent per conubia</p>
  </div>
  <div class="why" style="left:860px;top:2140px">
    <svg width="44" height="44" viewBox="0 0 44 44"><circle cx="22" cy="20" r="13" fill="none" stroke="#222" stroke-width="2.5"/><circle cx="22" cy="20" r="5" fill="none" stroke="#222" stroke-width="2.5"/><path d="M16 38h12" stroke="#222" stroke-width="2.5"/></svg>
    <h3>LIVE SUPPORT</h3>
    <p>Donec varius sodales orci. Class aptent taciti sociosqu ad litora torquent per conubia</p>
  </div>
</section>

<section class="fleet">
  <div class="fleet-bg"></div>
  <h2 class="section-title" style="top:2462px">Our Fleet</h2>

  <div class="fleet-photo" style="left:111px"><div class="car-shape" role="img" aria-label="Black sports sedan" style="background:linear-gradient(180deg,#444,#111)"></div></div>
  <div class="fleet-photo" style="left:362px"><div class="car-shape" role="img" aria-label="Silver hatchback" style="background:linear-gradient(180deg,#ddd,#888)"></div></div>
  <div class="fleet-photo" style="left:610px"><div class="car-shape" role="img" aria-label="Black hatchback" style="background:linear-gradient(180deg,#555,#151515)"></div></div>
  <div class="fleet-photo" style="left:861px"><div class="car-shape" role="img" aria-label="Silver hatchback" style="background:linear-gradient(180deg,#ddd,#888)"></div></div>

  <div class="price" style="left:111px">From $110</div>
  <div class="price" style="left:362px">From $110</div>
  <div class="price" style="left:610px">From $110</div>
  <div class="price" style="left:861px">From $110</div>

  <div class="car-name" style="left:119px">Bravara Grand &nbsp;Sedan</div>
  <div class="car-name" style="left:370px">Corvell Esquire</div>
  <div class="car-name" style="left:618px">Linden LX</div>
  <div class="car-name" style="left:869px">Bravara Grand &nbsp;Sedan</div>

  <div class="car-spec" style="left:119px;top:2793px"><i></i>4 Passengers</div>
  <div class="car-spec" style="left:370px;top:2793px"><i></i>4 Passengers</div>
  <div class="car-spec" style="left:618px;top:2793px"><i></i>4 Passengers</div>
  <div class="car-spec" style="left:869px;top:2793px"><i></i>4 Passengers</div>
  <div class="car-spec" style="left:119px;top:2822px"><i></i>2 Bags</div>
  <div class="car-spec" style="left:370px;top:2822px"><i></i>2 Bags</div>
  <div class="car-spec" style="left:618px;top:2822px"><i></i>2 Bags</div>
  <div class="car-spec" style="left:869px;top:2822px"><i></i>2 Bags</div>

  <div class="btn-outline" style="left:115px;top:2861px;width:106px;height:30px">BOOK NOW</div>
  <div class="btn-outline" style="left:366px;top:2861px;width:106px;height:30px">BOOK NOW</div>
  <div class="btn-outline" style="left:614px;top:2861px;width:106px;height:30px">BOOK NOW</div>
  <div class="btn-outline" style="left:865px;top:2861px;width:106px;height:30px">BOOK NOW</div>

  <svg class="abs" style="left:576px;top:2936px" width="48" height="8" viewBox="0 0 48 8"><circle cx="4" cy="4" r="3.5" fill="#c8102e"/><circle cx="24" cy="4" r="3.5" fill="#c8102e"/><circle cx="44" cy="4" r="3.5" fill="#c8102e"/></svg>
</section>

<section class="cta">
  <div class="abs" role="img" aria-label="Chauffeur in sunglasses beside a dark car" style="inset:0"></div>
  <h2>CHAUFFEUR HAS A WIDE ARRAY OF PRICING OPTIONS TO MEET ALL OF YOUR NEEDS</h2>
  <div class="btn-red" style="left:535px;top:126px;width:124px;height:28px;font-size:11px">VIEW PRICING</div>
</section>

<section class="contact">
  <div class="info" style="top:3300px"><h4>ADDRESS</h4><p>48 HARROWGATE LANE, MILLBROOK,<br>MB 214, WESTFORD, UK</p></div>
  <div class="info" style="top:3412px"><h4>EMAIL</h4><p>INFO@BROOKVANE.CO.UK</p></div>
  <div class="info" style="top:3492px"><h4>PHONE</h4><p>07700 900418</p></div>
  <div class="info" style="top:3574px"><h4>FOLLOW US</h4></div>
  <div class="social" style="left:216px"><i></i></div>
  <div class="social" style="left:270px"><i></i></div>
  <div class="social" style="left:321px"><i></i></div>
  <div class="social" style="left:374px"><i></i></div>

  <div class="contact-title">CONTACT</div>
  <div class="input" style="top:3339px;height:36px">Enter your name</div>
  <div class="input" style="top:3391px;height:36px">Enter your email</div>
  <div class="input" style="top:3442px;height:36px">Phone Number</div>
  <div class="input" style="top:3496px;height:82px;align-items:flex-start;padding-top:12px">Message</div>
  <div class="btn-red" style="left:613px;top:3592px;width:92px;height:32px;font-size:11px">SUBMIT</div>
</section>

<footer class="footer">
  <div class="brand"><span class="brand-dot"></span>Brookvane</div>
  <nav class="nav"><span>Home</span><span>Services</span><span>About Us</span><span>VIP</span><span>Contact us</span></nav>
  <div class="copy">© 2018 www.brookvane.co.uk | All Rights Reserved</div>
</footer>

</body>
</html>
```